"The Wandering Mentor", a Higher Ed blogger, would like a wordpress design

I would like a wordpress design for blogs written by "The Wandering Mentor." that can be easily expanded by me once the initial design is complete.

Here is context which I would like included on the Home/Welcome page: "I started The Wandering Mentor in 2021 to write about the practice of academic advising through the lens of horsemanship. After one year of developing skills as a brand new equestrian, I couldn’t help but notice the similarities between my vocation as an academic advisor and my avocation as a budding equestrian. I hope my musings about my journey in two very different fields will cultivate curiosity, widen your aperture and ignite academic advisors to take their practice to the next level. "

The wordpress will primarily have blogs by myself or guest bloggers writing about academic advising for advisors, but I may widen my audience to include students and families. I'd like to have readers submit questions that I can answer. Depending on interest, I may want to have a section on Horsemanship but that is not truly the focus of this site.

I'd like the feel of the site to be positive, fresh, modern (but not too wild), with the emphasis on Higher Ed/Academic Advising as opposed to equestrian pursuits. I don't want it to feel clunky and blocky like some sites that have to do with education. I'm hoping that readers will have some "aha" moments after reading some of the posts.

I have included my logo files

```html
<!DOCTYPE html>
<html lang="en">
<head>
<meta charset="utf-8">
<title>The Wandering Mentor</title>
<link rel="stylesheet" href="https://fonts.googleapis.com/css2?family=Roboto:wght@400;500;700&display=swap">
<style>
:root{
  --gold:#d4ad6a;
  --gold-dark:#c39a55;
  --ink:#1b1b1b;
  --text:#333;
  --cream:#fdf7ef;
  --white:#fff;
  --footer:#1c1c1c;
}
*{box-sizing:border-box;margin:0;padding:0}
html,body{width:1200px;height:4240px;overflow:hidden}
body{position:relative;background:var(--white);font-family:'Roboto',Arial,sans-serif;color:var(--text)}
.abs{position:absolute}
.btn{position:absolute;display:flex;align-items:center;justify-content:center;background:var(--gold);color:#fff;font-weight:700;font-size:14px;letter-spacing:.3px;border-radius:30px;text-transform:uppercase}
.btn-outline{position:absolute;display:flex;align-items:center;justify-content:center;border:1.5px solid var(--gold);color:var(--gold);font-weight:500;font-size:13px;border-radius:30px;text-transform:uppercase;background:transparent}

/* header */
.brand{left:98px;top:26px;width:220px;text-align:center}
.brand-mark{width:44px;height:44px;border:2px solid var(--gold);border-radius:50%;margin:0 auto 6px}
.brand-name{font-size:19px;color:var(--ink)}
.follow{left:592px;top:30px;display:flex;align-items:center;gap:16px;font-size:14px;color:var(--ink)}
.follow .rule{width:40px;height:1.5px;background:var(--ink)}
.follow .dot{width:12px;height:12px;border-radius:50%;background:var(--ink)}
.join{left:979px;top:20px;width:119px;height:38px;border-radius:2px;font-weight:500}
.nav{top:76px;left:472px;width:626px;display:flex;justify-content:space-between;font-size:15px;font-weight:500;color:var(--ink)}
.nav .active{color:var(--gold)}

/* hero */
.hero-photo{left:0;top:112px;width:1200px;height:640px;background:linear-gradient(180deg,#cfd3d6 0%,#c2c0b8 28%,#a88458 52%,#8c6a3e 72%,#5f7a3a 88%,#6c8a40 100%)}
.hero-title{left:118px;top:240px;font-size:64px;line-height:64px;font-weight:700;color:var(--ink)}
.hero-lead{left:118px;top:376px;width:460px;font-size:14px;line-height:25px;font-weight:500;color:var(--ink)}
.hero-btn{left:120px;top:440px;width:156px;height:46px}
.dots{left:560px;top:743px;display:flex;gap:12px}
.dots span{width:12px;height:12px;border-radius:50%;border:1.5px solid #888}
.dots .on{background:#888}

/* welcome */
.welcome-mark{left:150px;top:860px;width:360px;height:340px;display:flex;align-items:center;justify-content:center}
.welcome-mark .ring{width:320px;height:320px;border:2px solid #3a3a3a;border-radius:50%;display:flex;align-items:center;justify-content:center;font-size:26px;font-weight:500;color:var(--ink);text-align:center;line-height:34px}
.welcome h2{left:609px;top:880px;font-size:32px;font-weight:500;color:var(--ink)}
.welcome p{left:611px;top:935px;width:446px;font-size:13.5px;line-height:27.5px;text-align:justify;color:#444}
.welcome .btn{left:609px;top:1154px;width:170px;height:46px}

/* services */
.services h2{left:0;width:1200px;top:1420px;text-align:center;font-size:40px;font-weight:700;color:var(--ink)}
.services .bar{left:566px;top:1474px;width:68px;height:2px;background:var(--gold)}
.photo{position:absolute;border-radius:2px}
.frame{position:absolute;border:1.5px solid var(--gold)}
.svc-title{font-size:29px;font-weight:700;color:var(--ink)}
.svc-date{font-size:15px;color:var(--gold);display:flex;align-items:center;gap:6px}
.svc-date i{display:inline-block;width:13px;height:12px;border:2px solid var(--gold);border-top-width:4px}
.svc-text{font-size:13px;line-height:25px;color:#444}
.timeline{left:599px;top:1577px;width:0;height:620px;border-left:1.5px dashed #999}
.tdot{width:16px;height:16px;border:2.5px solid var(--gold);border-radius:50%;background:var(--cream)}
.tmark{left:576px;top:2172px;width:46px;height:46px;border:1.5px solid #666;border-radius:50%;background:var(--cream)}

/* horsemanship */
.horse-circle{left:109px;top:2466px;width:476px;height:484px;border-radius:50%;background:radial-gradient(circle at 50% 55%,#8a5030 0%,#6e4a35 35%,#8f7b6a 70%,#5a4a3e 100%)}
.horse h2{left:653px;top:2552px;font-size:35px;font-weight:500;color:var(--ink)}
.horse p{left:655px;top:2612px;width:446px;font-size:13.5px;line-height:27.5px;color:#444}
.horse .when{left:662px;top:2788px;font-size:15px;color:var(--ink)}
.horse .btn{left:660px;top:2833px;width:171px;height:44px}

/* why */
.why h2{left:0;width:1200px;top:3128px;text-align:center;font-size:36px;font-weight:700;color:var(--ink)}
.why .sub{left:0;width:1200px;top:3184px;text-align:center;font-size:16px;color:#444}
.feature{position:absolute;top:3262px;width:310px;text-align:center}
.feature svg{display:block;margin:0 auto}
.feature h3{margin-top:40px;font-size:19px;font-weight:700;color:var(--ink)}
.feature p{margin-top:16px;font-size:15px;line-height:25.5px;color:#444}

/* footer */
.footer-bg{left:0;top:3600px;width:1200px;height:640px}
.footer-mark{left:530px;top:3690px;width:140px;height:140px;border:2px solid #fff;border-radius:50%;display:flex;align-items:center;justify-content:center;text-align:center;font-size:16px;line-height:22px;color:#fff}
.news h3{left:120px;top:3872px;font-size:23px;font-weight:500;color:#fff}
.news h3::after{content:"";display:block;width:50px;height:2px;background:var(--gold);margin-top:10px}
.news p{left:120px;top:3937px;width:480px;font-size:13px;line-height:19px;color:#fff}
.field{position:absolute;left:120px;width:478px;height:40px;background:#fff;padding:0 12px;display:flex;align-items:center;font-size:13px;color:#444}
.check{left:120px;top:4106px;display:flex;align-items:center;gap:6px;font-size:12px;color:#fff}
.check i{width:12px;height:12px;background:#fff;display:inline-block}
.submit{left:481px;top:4108px;width:117px;height:42px;border-radius:0;font-size:15px}
.divider{left:665px;top:3885px;width:1px;height:247px;background:#555}
.about h4{left:726px;top:3888px;font-size:14px;font-weight:700;color:var(--gold)}
.about p{left:726px;top:3913px;width:360px;font-size:13px;line-height:24px;color:#fff}
.social{left:722px;top:4112px;display:flex;gap:26px;align-items:center}
.social span{width:18px;height:18px;border-radius:50%;background:#fff;display:block}
.copyright{left:0;width:1200px;top:4205px;text-align:center;font-size:14px;color:#fff}
</style>
</head>
<body>

<!-- header -->
<div class="abs brand">
  <div class="brand-mark"></div>
  <div class="brand-name">The Wandering Mentor</div>
</div>
<div class="abs follow">
  <span>Follow on</span><span class="rule"></span>
  <span class="dot"></span><span class="dot"></span><span class="dot"></span><span class="dot"></span><span class="dot"></span>
  <svg width="16" height="12" viewBox="0 0 16 12"><rect x="0.5" y="0.5" width="15" height="11" fill="#1b1b1b"/><path d="M1 1l7 6 7-6" stroke="#fff" fill="none"/></svg>
  <svg width="15" height="15" viewBox="0 0 15 15"><circle cx="6" cy="6" r="4.5" stroke="#1b1b1b" stroke-width="2" fill="none"/><path d="M9.5 9.5l4 4" stroke="#1b1b1b" stroke-width="2"/></svg>
</div>
<div class="btn join">Join Now</div>
<nav class="abs nav">
  <span class="active">HOME</span><span>ABOUT</span><span>SERVICES</span><span>BLOG</span><span>CONTACT</span>
</nav>

<!-- hero -->
<section class="abs hero-photo" role="img" aria-label="Photograph of a domed historic university library under a cloudy sky with a green lawn"></section>
<svg class="abs" style="left:0;top:600px" width="1200" height="160" viewBox="0 0 1200 160">
  <path d="M0 30 Q600 210 1200 20 L1200 160 L0 160Z" fill="#fff"/>
  <path d="M0 30 Q300 120 600 126" stroke="#1b1b1b" stroke-width="14" fill="none"/>
  <path d="M600 126 Q900 122 1200 20" stroke="#d4ad6a" stroke-width="10" fill="none"/>
</svg>
<h1 class="abs hero-title">THE WANDERING<br>MENTOR</h1>
<p class="abs hero-lead">Lorem ipsum dolor sit amet, consectetur adipiscing elit, sed do eiusmod tempor incididunt ut labore et dolore</p>
<div class="btn hero-btn">Get Started</div>
<svg class="abs" style="left:56px;top:362px" width="20" height="36" viewBox="0 0 20 36"><path d="M16 2L4 18l12 16" stroke="#fff" stroke-width="2" fill="none"/></svg>
<svg class="abs" style="left:1112px;top:362px" width="20" height="36" viewBox="0 0 20 36"><path d="M4 2l12 16L4 34" stroke="#fff" stroke-width="2" fill="none"/></svg>
<div class="abs dots"><span></span><span class="on"></span><span></span><span></span></div>

<!-- welcome -->
<div class="abs welcome-mark"><div class="ring">The<br>Wandering<br>Mentor</div></div>
<section class="welcome">
  <h2 class="abs">Welcome The Wandering Mentor</h2>
  <p class="abs">I started The Wandering Mentor in 2021 to write about the practice of academic advising through the lens of horsemanship. After one year of developing skills as a brand new equestrian, I couldn’t help but notice the similarities between my vocation as an academic advisor and my avocation as a budding equestrian. I hope my musings about my journey in two very different fields will cultivate curiosity, widen your aperture and ignite academic advisors to take their practice to the next level.</p>
  <div class="btn">Read More</div>
</section>

<!-- services -->
<svg class="abs" style="left:0;top:1262px" width="1200" height="1160" viewBox="0 0 1200 1160">
  <path d="M0 0 Q600 180 1200 0 L1200 1148 Q600 1000 0 1148Z" fill="#fdf7ef"/>
  <path d="M0 0 Q600 180 1200 0" stroke="#1b1b1b" stroke-width="3" fill="none"/>
  <path d="M0 1148 Q600 1000 1200 1148" stroke="#1b1b1b" stroke-width="3" fill="none"/>
</svg>
<section class="services">
  <h2 class="abs">OUR SERVICES</h2>
  <div class="abs bar"></div>

  <div class="frame" style="left:155px;top:1547px;width:347px;height:275px"></div>
  <div class="photo" role="img" aria-label="Photograph of an advisor and a student reviewing papers at a table" style="left:166px;top:1529px;width:382px;height:283px;background:linear-gradient(120deg,#8a8f86 0%,#b8a48e 40%,#7fb0cc 70%,#6d5040 100%)"></div>
  <div class="abs svc-title" style="left:658px;top:1528px">ACADEMIC ADVISOR</div>
  <div class="abs svc-date" style="left:658px;top:1572px"><i></i>21 SEP 2021</div>
  <p class="abs svc-text" style="left:658px;top:1603px;width:400px">Lorem ipsum dolor sit amet, consectetur adipiscintd do eiusmod tempor incididunt ut labore et dolore magna alsum suspendisse ultrices gravida. Risus coLorem ipsum dolor sit amet, consectetur adipiscintd do eiusmod tempor incididuntLorem ipsum dolor sit amet, consectetur adipiscintd do eiusmod</p>
  <div class="btn-outline" style="left:658px;top:1748px;width:140px;height:36px">Read More</div>

  <div class="timeline abs"></div>
  <div class="abs tdot" style="left:592px;top:1568px"></div>
  <div class="abs tdot" style="left:592px;top:1969px"></div>
  <div class="abs tmark"></div>

  <div class="abs svc-title" style="left:155px;top:1928px">BUDDING EQUESTRIAN</div>
  <div class="abs svc-date" style="left:155px;top:1972px"><i></i>21 SEP 2021</div>
  <p class="abs svc-text" style="left:155px;top:2003px;width:400px">Lorem ipsum dolor sit amet, consectetur adipiscintd do eiusmod tempor incididunt ut labore et dolore magna alsum suspendisse ultrices gravida. Risus coLorem ipsum dolor sit amet, consectetur adipiscintd do eiusmod tempor incididuntLorem ipsum dolor sit amet, consectetur adipiscintd do eiusmod</p>
  <div class="btn-outline" style="left:151px;top:2146px;width:139px;height:37px">Read More</div>

  <div class="frame" style="left:696px;top:1950px;width:349px;height:272px"></div>
  <div class="photo" role="img" aria-label="Photograph of a rider on a chestnut horse" style="left:652px;top:1929px;width:382px;height:283px;background:linear-gradient(160deg,#dfe3e0 0%,#c9ccc8 35%,#9a5a30 65%,#6f6a5e 100%)"></div>
</section>

<!-- horsemanship -->
<svg class="abs" style="left:104px;top:2460px" width="486" height="494" viewBox="0 0 486 494"><path d="M10 220 A238 242 0 0 1 250 5" stroke="#d4ad6a" stroke-width="8" fill="none"/></svg>
<div class="abs horse-circle" role="img" aria-label="Photograph of a rider in a helmet on a brown and white horse in an arena"></div>
<section class="horse">
  <h2 class="abs">Horsemanship</h2>
  <p class="abs">Lorem ipsum dolor sit amet, consectetur adipiscing elit, sed do eiusmod tempor incididunt ut labore et dolore magna ipsum suspendisse ultrices gravida. Risus commodo viverra maecenas accumsan lacus vel facilisis. Lorem ipsum dolor sit amet, consectetur adipiscing elit, sed do eiusmod tempor incididunt ut labore et doloqua. Quis ipsum suspendisse ultrices gravida. Risus commodo viverra maecenas</p>
  <div class="abs when">14 SPE 2021, 10: 00 AM</div>
  <div class="btn">Read More</div>
</section>

<!-- why -->
<svg class="abs" style="left:0;top:3000px" width="1200" height="640" viewBox="0 0 1200 640">
  <path d="M0 4 Q600 140 1200 4 L1200 640 L0 640Z" fill="#fdf7ef"/>
  <path d="M0 4 Q600 140 1200 4" stroke="#1b1b1b" stroke-width="4" fill="none"/>
</svg>
<section class="why">
  <h2 class="abs">Why The Wandering Mentor</h2>
  <div class="abs sub">sit voluptatem accusantium doloremque laudantium totam rem aperiam</div>
  <div class="feature" style="left:95px">
    <svg width="80" height="76" viewBox="0 0 80 76" fill="none" stroke="#d4ad6a" stroke-width="2.5"><circle cx="40" cy="30" r="22"/><circle cx="40" cy="30" r="9"/><path d="M8 60l16-10 16 10 16-10 16 10"/></svg>
    <h3>FINIBUS BONORUM ET</h3>
    <p>Lorem ipsum dolor sit amet, ecttur adipiscing elit, sed do eiusd tempor incididunt ut labore et doloreagna alua. Quis ipsum suspendisse ultrs gravida. Risus codo viverra</p>
  </div>
  <div class="feature" style="left:444px">
    <svg width="84" height="76" viewBox="0 0 84 76" fill="none" stroke="#d4ad6a" stroke-width="2.5"><path d="M4 26L42 10l38 16-38 16z"/><path d="M20 34v18c0 8 44 8 44 0V34"/><path d="M12 30v26"/></svg>
    <h3>FINIBUS BONORUM ET</h3>
    <p>Lorem ipsum dolor sit amet, ecttur adipiscing elit, sed do eiusd tempor incididunt ut labore et doloreagna alua. Quis ipsum suspendisse ultrs gravida. Risus codo viverra</p>
  </div>
  <div class="feature" style="left:791px">
    <svg width="80" height="76" viewBox="0 0 80 76" fill="none" stroke="#d4ad6a" stroke-width="2.5"><path d="M40 4l22 8v16c0 14-10 22-22 26-12-4-22-12-22-26V12z"/><path d="M30 28l7 7 13-13"/><path d="M6 62h22l12 8 34-10"/></svg>
    <h3>FINIBUS BONORUM ET</h3>
    <p>Lorem ipsum dolor sit amet, ecttur adipiscing elit, sed do eiusd tempor incididunt ut labore et doloreagna alua. Quis ipsum suspendisse ultrs gravida. Risus codo viverra</p>
  </div>
</section>

<!-- footer -->
<svg class="abs footer-bg" width="1200" height="640" viewBox="0 0 1200 640">
  <path d="M0 150 Q500 -20 1200 130 L1200 640 L0 640Z" fill="#1c1c1c"/>
  <path d="M760 30 Q1000 40 1200 130" stroke="#d4ad6a" stroke-width="12" fill="none"/>
</svg>
<div class="abs footer-mark">The<br>Wandering<br>Mentor</div>
<section class="news">
  <h3 class="abs">Sign Up to The Wandering Mentor Newsletter!</h3>
  <p class="abs">Enter your email and ge the very latest news from The Wandering Mentor: tips and insights, announcements, events, and more! Sign up now!</p>
  <div class="field" style="top:3992px">Email</div>
  <div class="field" style="top:4049px">Phone</div>
  <div class="abs check"><i></i>Send me news and updates</div>
  <div class="btn submit">Submit</div>
</section>
<div class="abs divider"></div>
<section class="about">
  <h4 class="abs">ABOUT THE WANDERING MENTOR</h4>
  <p class="abs">Lorem ipsum dolor sit amet, consectetur adipiscing elit, sed do eiusmod tempor incididunt ut labore et doagna aliqua. Ut enim ad minim veniam, quis nostrud exercitan ullamco laboris nisi ut aliquip ex ea commodo consequat . Duis aute irure dolor in reprehenderit in voluptate velsse cillum dolore eu fugiat nulla pariatur. Excepteur sint aecat cupidatat non proident, sunt in culpa</p>
</section>
<div class="abs social">
  <svg width="24" height="24" viewBox="0 0 24 24" fill="#fff"><circle cx="18" cy="5" r="4"/><circle cx="6" cy="12" r="4"/><circle cx="18" cy="19" r="4"/><path d="M6 12L18 5M6 12l12 7" stroke="#fff" stroke-width="2"/></svg>
  <span></span><span></span><span></span><span></span><span></span>
  <svg width="18" height="14" viewBox="0 0 18 14"><rect width="18" height="14" fill="#fff"/><path d="M1 1l8 7 8-7" stroke="#1c1c1c" stroke-width="1.5" fill="none"/></svg>
</div>
<div class="abs copyright">Copyright © 2021 The Wandering Mentor All rights reserved.</div>

</body>
</html>
```